IT Company based on Biology Business Needs a Business Card Design

We need a business card design for a new company called 'Lumen CELL'. We develop the machine learning solutions especially focused on deep learning algorithms for biology industry. Our initial product is a vision detection on biological images to help doctors diagnose the symptoms. We would like to see designs that use the color green.

Industry/Entity Type

Business

```html
<!DOCTYPE html>
<html lang="en">
<head>
<meta charset="UTF-8">
<title>Lumen CELL — Business Card</title>
<link href="https://fonts.googleapis.com/css2?family=Roboto:wght@300;400;500&display=swap" rel="stylesheet">
<style>
  :root {
    --backdrop: #1c1c1c;
    --card-white: #ffffff;
    --pattern-grey: #e6e7e8;
    --green-dark: #2f9248;
    --green-mid: #4ea84e;
    --green-light: #7cc04a;
    --brand-green: #74bf44;
    --icon-green: #2e8f46;
    --text-dark: #333333;
    --text-body: #3d3d3d;
  }
  * { margin: 0; padding: 0; box-sizing: border-box; }
  html, body {
    width: 1200px;
    height: 1200px;
    overflow: hidden;
    background: var(--backdrop);
    font-family: "Roboto", Arial, sans-serif;
  }
  .card {
    position: absolute;
    left: 216px;
    width: 765px;
    height: 467px;
    overflow: hidden;
  }
  .card--front { top: 105px; background: var(--card-white); }
  .card--back {
    top: 616px;
    background: linear-gradient(160deg, var(--green-dark) 0%, var(--green-mid) 50%, var(--green-light) 100%);
  }
  .decor-area {
    position: absolute;
    left: 0;
    top: 0;
    width: 400px;
    height: 467px;
  }
  .card--front .decor-area {
    background: linear-gradient(135deg, var(--pattern-grey) 0%, #f1f2f2 55%, rgba(255,255,255,0) 100%);
    clip-path: polygon(0 45%, 38% 0, 100% 0, 30% 100%, 0 100%);
  }
  .card--back .decor-area {
    background: linear-gradient(135deg, rgba(255,255,255,0.16) 0%, rgba(255,255,255,0.06) 70%, rgba(255,255,255,0) 100%);
    clip-path: polygon(0 45%, 38% 0, 100% 0, 30% 100%, 0 100%);
  }
  .brand-name {
    position: absolute;
    font-weight: 500;
    letter-spacing: -1px;
    white-space: nowrap;
    line-height: 1;
  }
  .card--front .brand-name {
    left: 484px;
    top: 82px;
    font-size: 36px;
    color: var(--brand-green);
  }
  .card--back .brand-name {
    left: 446px;
    top: 288px;
    font-size: 54px;
    color: var(--card-white);
  }
  .person {
    position: absolute;
    left: 442px;
    top: 196px;
    color: var(--text-dark);
  }
  .person__name { font-size: 27px; font-weight: 400; line-height: 1.1; }
  .person__title { font-size: 17px; font-weight: 400; margin-top: 4px; }
  .contacts {
    position: absolute;
    left: 411px;
    top: 275px;
    list-style: none;
    color: var(--text-body);
    font-size: 17px;
    font-weight: 400;
  }
  .contacts li {
    display: flex;
    align-items: flex-start;
    line-height: 21.5px;
    margin-bottom: 4px;
  }
  .contacts svg {
    width: 18px;
    height: 18px;
    margin-top: 2px;
    margin-right: 11px;
    flex: none;
    fill: var(--icon-green);
  }
</style>
</head>
<body>

<section class="card card--front">
  <div class="decor-area" role="img" aria-label="Soft grey molecular strand decoration"></div>
  <div class="brand-name">Lumen CELL</div>
  <div class="person">
    <div class="person__name">Aaron Whitlock</div>
    <div class="person__title">President</div>
  </div>
  <ul class="contacts">
    <li>
      <svg viewBox="0 0 24 24" aria-hidden="true"><path d="M12 2a7 7 0 0 0-7 7c0 5 7 13 7 13s7-8 7-13a7 7 0 0 0-7-7zm0 9.5A2.5 2.5 0 1 1 12 6.5a2.5 2.5 0 0 1 0 5z"/></svg>
      <span>Address will go here<br>B-14, Orchard Lane, Fernside<br>Addt. information on location</span>
    </li>
    <li>
      <svg viewBox="0 0 24 24" aria-hidden="true"><path d="M6.6 10.8a15.1 15.1 0 0 0 6.6 6.6l2.2-2.2a1 1 0 0 1 1-.25 11.4 11.4 0 0 0 3.6.57 1 1 0 0 1 1 1V20a1 1 0 0 1-1 1A17 17 0 0 1 3 4a1 1 0 0 1 1-1h3.5a1 1 0 0 1 1 1c0 1.25.2 2.45.57 3.57a1 1 0 0 1-.25 1z"/></svg>
      <span>(555) 214-0386</span>
    </li>
    <li>
      <svg viewBox="0 0 24 24" aria-hidden="true"><path d="M2 5h20v14H2z M2 5l10 8 10-8" fill="none" stroke="#2e8f46" stroke-width="2"/><path d="M3 6l9 7 9-7z"/></svg>
      <span>info@lumencell.com</span>
    </li>
    <li>
      <svg viewBox="0 0 24 24" aria-hidden="true"><circle cx="5" cy="19" r="2.2"/><path d="M3 11a10 10 0 0 1 10 10h-2.5A7.5 7.5 0 0 0 3 13.5zM3 4a17 17 0 0 1 17 17h-2.5A14.5 14.5 0 0 0 3 6.5z"/></svg>
      <span>www.lumencell.com</span>
    </li>
  </ul>
</section>

<section class="card card--back">
  <div class="decor-area" role="img" aria-label="Outlined molecular strand decoration in white"></div>
  <div class="brand-name">Lumen CELL</div>
</section>

</body>
</html>
```